Hydrographic business needs a business card that reaches hunters and off-road enthusiasts

We need a business card for a new hydrographics company catering to customers such as hunters, off-road ATV riders and custom vehicle enthusiasts. A western theme is preferred but professional. Our service should be thought of as upper end graphic design on firearms, off road vehicles, motorcycles, etc... See www.caldorfx.com for ideas on patterns, colors, etc...

Target Market(s)

Hunters, off road enthusiasts, custom car enthusiasts, motorcycle riders...

Industry/Entity Type

Graphic Design

```html
<!DOCTYPE html>
<html lang="en">
<head>
<meta charset="utf-8">
<title>Caldor Hydro Graphics – Business Card</title>
<link rel="stylesheet" href="https://fonts.googleapis.com/css2?family=Rye&family=Libre+Baskerville&family=Source+Sans+3:wght@400;600;700&display=swap">
<style>
  :root {
    --stage: #5c0b0b;
    --card-cream: #f2ddaa;
    --card-cream-back: #ece0c2;
    --panel-dark: #4b3b22;
    --panel-dark-edge: #3a2d19;
    --panel-orange: #e7a131;
    --gold: #e8c77a;
    --gold-deep: #d6b262;
    --ink: #3d2e1a;
    --cream-text: #f7e9c6;
    --logo-disc: #cbbfae;
  }
  * { margin: 0; padding: 0; box-sizing: border-box; }
  html, body { width: 1200px; height: 970px; overflow: hidden; }
  body { background: var(--stage); position: relative; font-family: "Source Sans 3", sans-serif; }

  .card { position: absolute; top: 88px; width: 446px; height: 742px; box-shadow: 0 6px 18px rgba(0,0,0,.45); }
  .card--front { left: 129px; background: var(--card-cream); }
  .card--back { left: 668px; height: 740px; background: var(--card-cream-back); }

  .panel { position: absolute; }
  .card--front .panel { left: 44px; top: 42px; width: 358px; height: 658px;
    background: radial-gradient(ellipse at 50% 40%, #5a4829 0%, var(--panel-dark) 55%, var(--panel-dark-edge) 100%); }
  .card--back .panel { left: 45px; top: 42px; width: 355px; height: 652px; background: var(--panel-orange); }

  .brand { position: absolute; border-radius: 50%; display: flex; align-items: center; justify-content: center; text-align: center; }
  .card--front .brand { left: 104px; top: 38px; width: 150px; height: 150px; background: #c9b48a; }
  .card--back .brand { left: 59px; top: 153px; width: 240px; height: 240px; background: var(--logo-disc); }
  .brand__name { font-family: "Source Sans 3", sans-serif; font-weight: 700; color: var(--ink); line-height: 1.1; }
  .card--front .brand__name { font-size: 20px; }
  .card--back .brand__name { font-size: 32px; }

  .tilted { position: absolute; left: 0; width: 100%; text-align: center; transform: rotate(-4deg); line-height: 1; white-space: nowrap; }
  .holder-name { top: 216px; font-family: "Rye", serif; font-size: 36px; color: var(--gold); }
  .star-row { position: absolute; left: 32px; width: 294px; height: 12px; background: var(--gold-deep); opacity: .8; transform: rotate(-4deg); }
  .star-row--top { top: 268px; }
  .star-row--bottom { top: 352px; }
  .phone { top: 291px; font-family: "Libre Baskerville", serif; font-size: 42px; color: var(--cream-text); }
  .tagline { top: 370px; font-family: "Libre Baskerville", serif; font-size: 12px; letter-spacing: .5px; color: var(--gold-deep); }

  .label { position: absolute; left: 0; width: 100%; text-align: center; font-family: "Libre Baskerville", serif; font-size: 12px; line-height: 1; color: var(--gold); }
  .label--postal { top: 446px; }
  .label--mail { top: 550px; }
  .address { position: absolute; left: 0; width: 100%; top: 462px; text-align: center; font-weight: 700; font-size: 24px; line-height: 33px; color: var(--cream-text); }

  .ribbon { position: absolute; }
  .ribbon svg { position: absolute; inset: 0; }
  .ribbon__text { position: absolute; inset: 0; display: flex; align-items: center; justify-content: center; color: var(--ink); font-size: 24px; }
  .ribbon--mail { left: 32px; top: 568px; width: 290px; height: 50px; }
  .ribbon--web { left: 35px; top: 400px; width: 286px; height: 44px; }
</style>
</head>
<body>

<section class="card card--front" aria-label="Card front">
  <div class="panel">
    <div class="brand"><span class="brand__name">Caldor Hydro<br>Graphics</span></div>
    <p class="tilted holder-name">Wade Caldor</p>
    <div class="star-row star-row--top" role="img" aria-label="Row of small gold stars"></div>
    <p class="tilted phone">214-555-0187</p>
    <div class="star-row star-row--bottom" role="img" aria-label="Row of small gold stars"></div>
    <p class="tilted tagline">I'M READY TO HELP YOU</p>

    <p class="label label--postal">MY POSTAL ADDRESS</p>
    <p class="address">212 Mesa Ridge Road<br>Cedar Bend, TX 75000</p>

    <p class="label label--mail">OR SEND ME E-MAIL</p>
    <div class="ribbon ribbon--mail">
      <svg viewBox="0 0 290 50" preserveAspectRatio="none" aria-hidden="true">
        <polygon points="0,4 290,0 280,25 290,50 0,48 10,26" fill="var(--gold-deep)"/>
      </svg>
      <span class="ribbon__text">wade@caldorfx.com</span>
    </div>
  </div>
</section>

<section class="card card--back" aria-label="Card back">
  <div class="panel">
    <div class="brand"><span class="brand__name">Caldor Hydro<br>Graphics</span></div>
    <div class="ribbon ribbon--web">
      <svg viewBox="0 0 286 44" preserveAspectRatio="none" aria-hidden="true">
        <polygon points="0,2 286,0 276,22 286,44 0,42 10,22" fill="var(--card-cream-back)"/>
      </svg>
      <span class="ribbon__text">www.caldorfx.com</span>
    </div>
  </div>
</section>

</body>
</html>
```